Boilerplate Management Organization Chart

"Our Management Approach is a deliberate step-by-step process and supports our Technical Approach detailed in proposal submission. The Management Approach covers all the human capital aspects for executing a contract—from contract award through to sustainment and/or transition of the contract to another company. It includes how we organize, hire, staff, train, and account for our contract employees—as well as their complete personal life-cycle management within the company."

We need this management approach to depict an amazing management process that demonstrates best practices of the project management body of knowledge. We need this vector image to be applicable to any proposal without making references to any other proposals. Generic names but using strong business language.
Updates

Thanks for all designs submitted thus far. Some have stuck to the original type of chart. We would like to see a completely different way to show the same information. It has to be able to be recognized and deciphered very quickly by people who might not necessarily want to look at it. It must draw them in and make it incredibly easy to distinguish a management approach that looks fresh, infallible, and easily implemented.

Target Market(s)

Federal space, Government organizations looking for procedural efficiencies,

Industry/Entity Type

Management

Requirements
Must have
• Must not take up more than 1/3 to 1/2 of printable page and be clear.
Should not have
• Not too much color, but should stick to some color palette of some interest.

```html
<!DOCTYPE html>
<html lang="en">
<head>
<meta charset="utf-8">
<title>Management Approach – Program Lifecycle Wheel</title>
<link href="https://fonts.googleapis.com/css2?family=Oswald:wght@600;700&family=Roboto+Condensed:wght@700&display=swap" rel="stylesheet">
<style>
  :root {
    --bg: #ffffff;
    --panel-line: #d6d6d6;
    --panel-stroke: #c4c4c4;
    --tag-text: #8a8a8a;
    --tag-stroke: #cfcfcf;
    --arrow: #b5b5b5;
    --crimson: #a8182f;
    --coral: #e0484e;
    --amber: #e49b2a;
    --lime: #7fb43d;
    --emerald: #1fae84;
    --teal: #1b8b94;
    --slate: #4b5152;
    --graphite: #5f6566;
    --label: #ffffff;
    --node: #ffffff;
    --node-text: #c9c9c9;
  }
  html, body {
    margin: 0;
    width: 1200px;
    height: 1200px;
    overflow: hidden;
    background: var(--bg);
  }
  .canvas { width: 1200px; height: 1200px; display: block; }
  .wedge-label {
    font-family: "Roboto Condensed", Arial, sans-serif;
    font-weight: 700;
    font-size: 19px;
    fill: var(--label);
    text-anchor: middle;
  }
  .node-number {
    font-family: "Roboto Condensed", Arial, sans-serif;
    font-weight: 700;
    font-size: 13px;
    fill: var(--node-text);
    text-anchor: middle;
  }
  .tag-text {
    font-family: "Oswald", Impact, sans-serif;
    font-weight: 700;
    fill: var(--tag-text);
    text-anchor: middle;
    letter-spacing: 1px;
  }
</style>
</head>
<body>
<svg class="canvas" viewBox="0 0 1200 1200" xmlns="http://www.w3.org/2000/svg">
  <defs>
    <pattern id="panel-stripes" width="8" height="6" patternUnits="userSpaceOnUse">
      <line x1="0" y1="3" x2="8" y2="3" stroke="var(--panel-line)" stroke-width="1.4"/>
    </pattern>
  </defs>

  <!-- backing panel -->
  <rect class="backing-panel" x="200" y="330" width="860" height="540" rx="18"
        fill="url(#panel-stripes)" stroke="var(--panel-stroke)" stroke-width="3"/>

  <!-- management approach tag with arrow -->
  <g class="tag-management">
    <polygon points="600,352 640,330 640,344 760,344 760,360 640,360 640,374" fill="var(--arrow)"/>
    <rect x="770" y="265" width="250" height="110" rx="10" fill="#fff" stroke="var(--tag-stroke)" stroke-width="4"/>
    <text class="tag-text" x="895" y="310" font-size="34">MANAGEMENT</text>
    <text class="tag-text" x="895" y="355" font-size="40">APPROACH</text>
  </g>

  <!-- lifecycle wheel -->
  <g class="wheel" transform="translate(540,610)">
    <g class="wedges">
      <path transform="rotate(0)"   fill="var(--coral)"   d="M0,-300 A300,300 0 0 1 212.1,-212.1 L91.9,-91.9 A130,130 0 0 0 0,-130 Z"/>
      <path transform="rotate(45)"  fill="var(--amber)"   d="M0,-290 A290,290 0 0 1 205.1,-205.1 L91.9,-91.9 A130,130 0 0 0 0,-130 Z"/>
      <path transform="rotate(90)"  fill="var(--lime)"    d="M0,-335 A335,335 0 0 1 236.9,-236.9 L91.9,-91.9 A130,130 0 0 0 0,-130 Z"/>
      <path transform="rotate(135)" fill="var(--emerald)" d="M0,-320 A320,320 0 0 1 226.3,-226.3 L91.9,-91.9 A130,130 0 0 0 0,-130 Z"/>
      <path transform="rotate(180)" fill="var(--teal)"    d="M0,-295 A295,295 0 0 1 208.6,-208.6 L91.9,-91.9 A130,130 0 0 0 0,-130 Z"/>
      <path transform="rotate(225)" fill="var(--graphite)" d="M0,-270 A270,270 0 0 1 190.9,-190.9 L91.9,-91.9 A130,130 0 0 0 0,-130 Z"/>
      <path transform="rotate(270)" fill="var(--slate)"   d="M0,-285 A285,285 0 0 1 201.5,-201.5 L91.9,-91.9 A130,130 0 0 0 0,-130 Z"/>
      <path transform="rotate(315)" fill="var(--crimson)" d="M0,-290 A290,290 0 0 1 205.1,-205.1 L91.9,-91.9 A130,130 0 0 0 0,-130 Z"/>
    </g>

    <!-- wedge labels -->
    <g class="wedge-labels">
      <text class="wedge-label" x="86" y="-200"><tspan x="86">Responsibility</tspan><tspan x="86" dy="21">Fixed</tspan></text>
      <text class="wedge-label" x="205" y="-80"><tspan x="205">Management</tspan><tspan x="205" dy="21">&amp; Oversight</tspan></text>
      <text class="wedge-label" x="225" y="80"><tspan x="225">Manning</tspan><tspan x="225" dy="21">the Team</tspan></text>
      <text class="wedge-label" x="95" y="215">Training</text>
      <text class="wedge-label" x="-85" y="200"><tspan x="-85">Professional</tspan><tspan x="-85" dy="21">Development</tspan></text>
      <text class="wedge-label" x="-190" y="90">Benefits</text>
      <text class="wedge-label" x="-200" y="-95"><tspan x="-200">Retention</tspan><tspan x="-200" dy="21">/ Quality of</tspan><tspan x="-200" dy="21">Life</tspan></text>
      <text class="wedge-label" x="-85" y="-205"><tspan x="-85">Sustainment</tspan><tspan x="-85" dy="21">/ Transition</tspan></text>
    </g>

    <!-- simple icons -->
    <g class="wedge-icons" fill="none" stroke="#fff" stroke-width="3" stroke-linecap="round">
      <circle cx="-85" cy="-245" r="13"/>
      <path d="M-92,-245 l6,6 l10,-12"/>
      <path d="M68,-245 l12,8 l12,-8 l12,8"/>
      <circle cx="190" cy="-120" r="13"/>
      <path d="M184,-120 l5,5 l8,-10"/>
      <circle cx="212" cy="45" r="6"/><circle cx="232" cy="45" r="6"/><circle cx="252" cy="45" r="6"/>
      <rect x="90" y="170" width="30" height="20"/>
      <path d="M85,195 h40"/>
      <circle cx="-85" cy="160" r="11"/>
      <path d="M-85,149 v-6 M-96,160 h-6 M-74,160 h6"/>
      <path d="M-210,70 v-10 M-200,70 v-16 M-190,70 v-22 M-215,72 h30"/>
      <path d="M-215,-145 q15,15 30,0"/>
    </g>

    <!-- centre ring -->
    <circle r="120" fill="#ffffff"/>
    <circle r="100" fill="none" stroke="#e3e3e3" stroke-width="10"/>
    <circle r="72" fill="#ffffff" stroke="var(--coral)" stroke-width="3"/>

    <!-- numbered nodes -->
    <g class="nodes" fill="var(--node)" stroke="#e0e0e0" stroke-width="2">
      <circle cx="38" cy="-92" r="13"/><circle cx="92" cy="-38" r="13"/>
      <circle cx="92" cy="38" r="13"/><circle cx="38" cy="92" r="13"/>
      <circle cx="-38" cy="92" r="13"/><circle cx="-92" cy="38" r="13"/>
      <circle cx="-92" cy="-38" r="13"/><circle cx="-38" cy="-92" r="13"/>
    </g>
    <g class="node-numbers">
      <text class="node-number" x="38" y="-87">1</text>
      <text class="node-number" x="92" y="-33">2</text>
      <text class="node-number" x="92" y="43">3</text>
      <text class="node-number" x="38" y="97">4</text>
      <text class="node-number" x="-38" y="97">5</text>
      <text class="node-number" x="-92" y="43">6</text>
      <text class="node-number" x="-92" y="-33">7</text>
      <text class="node-number" x="-38" y="-87">8</text>
    </g>
  </g>

  <!-- program evaluation tag -->
  <g class="tag-evaluation">
    <rect x="800" y="800" width="320" height="150" rx="12" fill="#fff" stroke="var(--tag-stroke)" stroke-width="4"/>
    <text class="tag-text" x="960" y="868" font-size="58">PROGRAM</text>
    <text class="tag-text" x="960" y="925" font-size="46">EVALUATION</text>
  </g>
</svg>
</body>
</html>
```